fernbrook stationary
cards + stationary
Professional
owen hale
director
52 pelham row
ashby vale
wexford shire
wd7 2lr
owen@fernbrookltd.co.uk
www.fernbrookltd.co.uk
require letter heading + comp slips
'retail and commercial solutions'
+ logo
font is 'goodtimes'

```html
<!DOCTYPE html>
<html lang="en">
<head>
<meta charset="utf-8">
<title>Fernbrook Stationery</title>
<link href="https://fonts.googleapis.com/css2?family=Orbitron:wght@700;900&family=Montserrat:wght@400;500&display=swap" rel="stylesheet">
<style>
  :root {
    --red: #d6262e;
    --red-light: #f04a3a;
    --blue-dark: #2b3a94;
    --blue-mid: #2e62c0;
    --blue-light: #35a6e6;
    --ink: #2d3a8c;
    --paper: #ffffff;
    --edge: #d9d9d9;
  }
  * { box-sizing: border-box; margin: 0; padding: 0; }
  html, body { width: 1200px; height: 1047px; overflow: hidden; background: var(--paper); }
  .canvas { position: relative; width: 1200px; height: 1047px; background: var(--paper); }
  address { font-style: normal; }

  .sheet { position: absolute; background: var(--paper); box-shadow: 0 0 0 1px var(--edge), 0 2px 6px rgba(0,0,0,.12); }

  .brand { position: absolute; display: flex; flex-direction: column; align-items: flex-start; }
  .brand-name { font-family: "Orbitron", sans-serif; font-weight: 900; color: var(--red); letter-spacing: 1px; line-height: 1; }
  .brand-tag { font-family: "Montserrat", sans-serif; font-weight: 500; color: var(--ink); text-transform: uppercase; letter-spacing: .6px; white-space: nowrap; margin-top: 3px; }
  .brand.on-blue .brand-name, .brand.on-blue .brand-tag { color: var(--paper); }

  .contact { position: absolute; font-family: "Montserrat", sans-serif; color: var(--ink); text-align: right; line-height: 1.35; white-space: nowrap; }

  .stripe-blue { position: absolute; left: 0; right: 0; background: linear-gradient(90deg, var(--blue-light), var(--blue-mid) 50%, var(--blue-dark)); }
  .stripe-red { position: absolute; left: 0; right: 0; background: linear-gradient(90deg, var(--red), var(--red-light) 50%, var(--red)); }

  /* letterhead */
  .letterhead { left: 100px; top: 51px; width: 1023px; height: 400px; }
  .letterhead .brand { left: 30px; top: 118px; }
  .letterhead .brand-name { font-size: 44px; }
  .letterhead .brand-tag { font-size: 8px; }
  .letterhead .contact { right: 108px; top: 80px; font-size: 11px; }
  .letterhead .contact .gap { height: 14px; }

  /* compliment slip below envelope */
  .slip { left: 100px; top: 860px; width: 723px; height: 129px; }
  .slip .stripe-blue { top: 84px; height: 18px; }
  .slip .stripe-red { top: 105px; height: 24px; }

  /* envelope */
  .envelope { position: absolute; left: 69px; top: 400px; width: 754px; height: 486px; }
  .envelope-flap { position: absolute; left: 0; top: 0; width: 754px; height: 100px; border-radius: 14px 14px 0 0; background: linear-gradient(90deg, var(--blue-light), var(--blue-mid) 55%, var(--blue-dark)); }
  .envelope-flap .brand { left: 270px; top: 18px; transform: rotate(180deg); }
  .envelope-flap .brand-name { font-size: 36px; }
  .envelope-flap .brand-tag { font-size: 7px; }
  .envelope-body { position: absolute; left: 0; top: 100px; width: 754px; height: 386px; background: var(--paper); box-shadow: 0 0 0 1px var(--edge), 0 2px 6px rgba(0,0,0,.12); }
  .envelope-body .brand { left: 18px; top: 82px; }
  .envelope-body .brand-name { font-size: 40px; }
  .envelope-body .brand-tag { font-size: 7.5px; }
  .envelope-body .return-address { position: absolute; left: 20px; top: 160px; font-family: "Montserrat", sans-serif; font-size: 11px; color: var(--ink); line-height: 1.35; }
  .envelope-body .stripe-blue { top: 318px; height: 18px; }
  .envelope-body .stripe-red { top: 338px; height: 22px; }

  /* business cards */
  .card-front { left: 851px; top: 443px; width: 286px; height: 243px; overflow: hidden; }
  .card-front .brand { left: 18px; top: 38px; }
  .card-front .brand-name { font-size: 26px; }
  .card-front .brand-tag { font-size: 5px; }
  .card-front .person { position: absolute; left: 110px; top: 100px; font-family: "Montserrat", sans-serif; color: var(--ink); }
  .card-front .person-name { font-size: 10px; font-weight: 500; }
  .card-front .person-role { font-size: 7px; margin-top: 2px; }
  .card-front .contact { right: 16px; top: 118px; font-size: 7px; }
  .card-front .stripe-blue { top: 210px; height: 12px; }
  .card-front .stripe-red { top: 224px; height: 19px; }

  .card-back { left: 851px; top: 714px; width: 286px; height: 178px; background: linear-gradient(90deg, var(--blue-light), var(--blue-mid) 55%, var(--blue-dark)); }
  .card-back .brand { left: 40px; top: 66px; }
  .card-back .brand-name { font-size: 30px; }
  .card-back .brand-tag { font-size: 5.5px; }
</style>
</head>
<body>
<main class="canvas">

  <section class="sheet letterhead" aria-label="Letterhead">
    <div class="brand">
      <span class="brand-name">FERNBROOK</span>
      <span class="brand-tag">air conditioning · refrigeration · electrical</span>
    </div>
    <address class="contact">
      52 pelham row<br>
      ashby vale<br>
      wexford shire, wd7 2lr<br>
      Phone: 01632 960514<br>
      www.fernbrookltd.co.uk
      <div class="gap"></div>
      Registration No: 4820193<br>
      vat reg no: 608334912<br>
      Incorporated 2004
    </address>
  </section>

  <section class="sheet slip" aria-label="Compliment slip">
    <div class="stripe-blue"></div>
    <div class="stripe-red"></div>
  </section>

  <section class="envelope" aria-label="Envelope">
    <div class="envelope-flap">
      <div class="brand on-blue">
        <span class="brand-name">FERNBROOK</span>
        <span class="brand-tag">air conditioning · refrigeration · electrical</span>
      </div>
    </div>
    <div class="envelope-body">
      <div class="brand">
        <span class="brand-name">FERNBROOK</span>
        <span class="brand-tag">air conditioning · refrigeration · electrical</span>
      </div>
      <address class="return-address">
        52 pelham row, ashby vale<br>
        wexford shire, wd7 2lr
      </address>
      <div class="stripe-blue"></div>
      <div class="stripe-red"></div>
    </div>
  </section>

  <section class="sheet card-front" aria-label="Business card front">
    <div class="brand">
      <span class="brand-name">FERNBROOK</span>
      <span class="brand-tag">air conditioning · refrigeration · electrical</span>
    </div>
    <div class="person">
      <div class="person-name">owen hale</div>
      <div class="person-role">director</div>
    </div>
    <address class="contact">
      52 pelham row<br>
      ashby vale<br>
      wexford shire, wd7 2lr<br>
      Phone: 01632 960514<br>
      Email: owen@fernbrookltd.co.uk<br>
      www.fernbrookltd.co.uk
    </address>
    <div class="stripe-blue"></div>
    <div class="stripe-red"></div>
  </section>

  <section class="sheet card-back" aria-label="Business card back">
    <div class="brand on-blue">
      <span class="brand-name">FERNBROOK</span>
      <span class="brand-tag">air conditioning · refrigeration · electrical</span>
    </div>
  </section>

</main>
</body>
</html>
```